KORVELTA Corporate Business Card

Modern business card design for company which focuses in the areas of Staffing, IT Consulting & Data Services. Please note: We are no longer using the IT subscript on the logo. All designs should have IT subscript removed.
Website: www.korveltait.example

```html
<!DOCTYPE html>
<html lang="en">
<head>
<meta charset="utf-8">
<title>KORVELTA Business Card</title>
<link href="https://fonts.googleapis.com/css2?family=Exo+2:ital,wght@0,600;1,600&family=Questrial&display=swap" rel="stylesheet">
<style>
  :root {
    --page: #2a2522;
    --card: #060606;
    --brand-blue: #35a9dc;
    --strip-blue: #3792d3;
    --band-light: #6ec6e8;
    --strip-grey: #c8c8c4;
    --text-light: #e6e6e6;
  }
  html, body {
    margin: 0;
    width: 1200px;
    height: 787px;
    overflow: hidden;
    background: var(--page);
  }
  .sheet {
    position: relative;
    width: 1200px;
    height: 787px;
    display: flex;
    align-items: center;
    justify-content: center;
    gap: 40px;
  }
  .card {
    position: relative;
    width: 560px;
    height: 320px;
    background: var(--card);
    border-radius: 16px;
    overflow: hidden;
    box-shadow: 0 10px 30px rgba(0,0,0,.45);
  }
  .wordmark {
    font-family: "Exo 2", sans-serif;
    font-weight: 600;
    color: var(--brand-blue);
    letter-spacing: 2px;
    display: flex;
    align-items: center;
    gap: 10px;
  }
  .wordmark .mark-square {
    width: 0.7em;
    height: 0.7em;
    background: var(--brand-blue);
  }
  /* front */
  .front .top-band {
    position: absolute;
    top: 0; right: 0;
    width: 180px; height: 22px;
    background: var(--band-light);
    border-bottom-left-radius: 12px;
  }
  .front .wordmark {
    position: absolute;
    top: 78px; left: 300px;
    font-size: 40px;
  }
  .front .name {
    position: absolute;
    top: 96px; left: 28px;
    margin: 0;
    font-family: "Exo 2", sans-serif;
    font-style: italic;
    font-weight: 600;
    font-size: 34px;
    color: var(--strip-blue);
  }
  .front .role {
    position: absolute;
    top: 140px; left: 30px;
    margin: 0;
    font-family: "Questrial", sans-serif;
    font-size: 13px;
    color: var(--text-light);
  }
  .front .divider {
    position: absolute;
    top: 162px; left: 28px;
    width: 490px; height: 2px;
    background: var(--strip-blue);
  }
  .front .contacts {
    position: absolute;
    top: 176px; left: 30px;
    margin: 0; padding: 0;
    list-style: none;
    font-family: "Questrial", sans-serif;
    font-size: 13px;
    line-height: 20px;
    color: var(--text-light);
  }
  .front .contacts li { display: flex; align-items: center; gap: 6px; }
  .front .contacts svg { width: 12px; height: 12px; }
  .front .address {
    position: absolute;
    right: 40px; top: 236px;
    margin: 0;
    text-align: right;
    font-family: "Questrial", sans-serif;
    font-style: normal;
    font-size: 14px;
    line-height: 20px;
    color: var(--text-light);
  }
  .front .bottom-strip {
    position: absolute;
    left: 0; bottom: 0;
    width: 560px; height: 24px;
  }
  /* back */
  .back .wordmark {
    position: absolute;
    top: 50%; left: 50%;
    transform: translate(-50%, -50%);
    font-size: 48px;
  }
</style>
</head>
<body>
<main class="sheet">
  <section class="card front" aria-label="Card front">
    <div class="top-band"></div>
    <div class="wordmark"><span class="mark-square"></span>KORVELTA</div>
    <h1 class="name">Dana Morrow</h1>
    <p class="role">President &amp; CEO</p>
    <div class="divider"></div>
    <ul class="contacts">
      <li>
        <svg viewBox="0 0 12 12" aria-hidden="true"><path d="M3 1 L5 3.5 L4 5 Q5.5 7.5 7 8 L8.5 7 L11 9 L9.5 11 Q4 10.5 1 3 Z" fill="var(--strip-blue)"/></svg>
        : 555 - 014 - 2270
      </li>
      <li>
        <svg viewBox="0 0 12 12" aria-hidden="true"><rect x="1" y="2.5" width="10" height="7" fill="none" stroke="var(--strip-blue)" stroke-width="1.3"/><path d="M1 2.5 L6 6.5 L11 2.5" fill="none" stroke="var(--strip-blue)" stroke-width="1.3"/></svg>
        : yourname@korveltait.example
      </li>
      <li>
        <svg viewBox="0 0 12 12" aria-hidden="true"><circle cx="6" cy="6" r="5" fill="none" stroke="var(--strip-blue)" stroke-width="1.3"/><path d="M1 6 H11 M6 1 Q3 6 6 11 M6 1 Q9 6 6 11" fill="none" stroke="var(--strip-blue)" stroke-width="1"/></svg>
        : www.korveltait.example
      </li>
    </ul>
    <address class="address">48 Larkfield Ave.<br>Brennton, IN 40190</address>
    <svg class="bottom-strip" viewBox="0 0 560 24" preserveAspectRatio="none" aria-hidden="true">
      <polygon points="0,4 300,4 310,24 0,24" fill="var(--strip-blue)"/>
      <polygon points="312,0 560,0 560,24 324,24" fill="var(--strip-grey)"/>
    </svg>
  </section>

  <section class="card back" aria-label="Card back">
    <div class="wordmark"><span class="mark-square"></span>KORVELTA</div>
  </section>
</main>
</body>
</html>
```